Kestrel - Adventurous, Fun, Exciting, Social Fitness Club needs a Biz Card/Promo Card with Attitude!

Kestrel... we're a fun, social, outdoor fitness club that needs not just a Business Card for our Trainers, but a mini-promo card that shows off our unique, innovative and cheeky personality/brand to the world!
Who Are We? We're a fun & social fitness club that prides ourselves on getting our members outdoors trying new, exciting physical activities in an effort to find joy in an active lifestyle, and sharing that experience with other like minded people. We offer:
- Personal Training (1-on-1 Fitness Training)
- Group Fitness Classes (Boxing, Pilates, etc)
- Boot Camps (Military Style - Sandbags, Ropes, Tyres, etc)
- Events (Fun Runs, Triathlons, Ocean Swims, Treks, etc)
- Adventures (Machu Picchu Trek, Rock Climbing, Kayaking, etc)
Our tag line is 'No Judgements. No Limits!' The business card should be bold, exciting, adventurous and innovative, illustrating the values of our brand: possibility, thirst for life, personal accomplishment & freedom. It should be fun, friendly & inviting... but not over the top. Think trendy surf brand style of look.
Forget your standard, boring, basic business cards that are just for contact details, our business card actually has 4 key purposes:
(1) Provide our contact details
(2) Highlight main benefits of what we do
(3) Lead generation via the offer of a Free Trial
(4) Direct people to "Like" us on Chatterbox
(see an example of business card/promo card combo attached)
THE DESIGN MUST COMPLIMENT & BE CONSISTENT IN LOOK WITH OUR NEWLY DESIGNED WEBSITE (see attached)
Look forward to seeing what you come up with! ;)

Reason: Extending by 5 days as still no design close enought to what we're after. Cheers

Industry/Entity Type
Fitness
Requirements
Must have
- - Please see attached Layout for all requirements
- Primary Colour to be orange + some limited use of darker orange shading (as per website)
- Want to see white dotted patten, dark orange "splat" (as per website).
Nice to have
- - size preference is 90 x 45mm.
Should not have
- - No rounded edges
- Only very minimal/no use of the "sun rays" effect (as used behind logo in the website design)

```html
<!DOCTYPE html>
<html lang="en">
<head>
<meta charset="utf-8">
<title>Kestrel Fitness Club – Business &amp; Promo Card</title>
<link rel="stylesheet" href="https://fonts.googleapis.com/css2?family=Jost:ital,wght@0,400;0,500;0,600;0,700;1,400&family=Oswald:wght@600;700&family=Roboto+Condensed:wght@700;800&display=swap">
<style>
  :root {
    --orange: #f26a21;
    --orange-deep: #d9530f;
    --black: #111111;
    --white: #ffffff;
    --yellow: #fff200;
    --grey-text: #333333;
    --ghost: rgba(150,150,150,0.10);
    --ghost-promo: rgba(120,40,0,0.08);
    --frame: #9a9a9a;
  }
  * { margin: 0; padding: 0; box-sizing: border-box; }
  html, body { width: 1118px; height: 1200px; overflow: hidden; background: var(--white); }
  body { position: relative; font-family: "Jost", "Century Gothic", sans-serif; }

  .card { position: absolute; left: 23px; width: 1075px; height: 539px; overflow: hidden; border: 1px solid var(--frame); }
  .card--contact { top: 28px; background: var(--white); }
  .card--promo { top: 628px; background: var(--orange); }
  .card__art { position: absolute; inset: 0; width: 100%; height: 100%; }
  .card__text { position: absolute; white-space: nowrap; }

  /* contact side */
  .ghost-art { position: absolute; left: 220px; top: 70px; width: 700px; height: 400px; background: var(--ghost); }
  .brand { left: 46px; top: 62px; display: flex; align-items: center; gap: 12px; font-weight: 700; font-size: 50px; color: var(--black); line-height: 1; }
  .brand__mark { width: 26px; height: 26px; background: var(--black); }
  .label { font-style: italic; font-weight: 400; font-size: 20px; color: var(--grey-text); }
  .label--orange { color: var(--orange); font-size: 18px; }
  .contact-label { left: 72px; top: 206px; }
  .person-name { left: 70px; top: 240px; font-size: 43px; font-weight: 500; color: var(--orange-deep); line-height: 1.2; }
  .person-role { left: 72px; top: 293px; font-style: italic; font-size: 20px; color: var(--grey-text); }
  .contact-list { left: 74px; top: 343px; list-style: none; font-size: 20px; font-weight: 600; color: var(--black); line-height: 34px; }
  .side-col { left: 745px; top: 28px; }
  .side-block { margin-bottom: 18px; }
  .side-block ul { list-style: none; font-weight: 600; color: var(--black); }
  .side-block--feature ul { font-size: 17px; line-height: 27px; }
  .side-block--tag ul, .side-block--services ul { font-size: 19px; line-height: 30px; }

  /* promo side */
  .ghost-art--promo { left: 300px; top: 210px; width: 560px; height: 300px; background: var(--ghost-promo); }
  .promo-title { left: 58px; top: 40px; font-family: "Oswald", "Impact", sans-serif; font-weight: 700; font-size: 82px; line-height: 1; color: var(--black); transform: rotate(-4deg); transform-origin: left bottom; text-shadow: -4px -5px 0 var(--yellow); letter-spacing: 0.5px; }
  .promo-strap { left: 32px; top: 142px; font-family: "Oswald", "Impact", sans-serif; font-weight: 600; font-size: 40px; line-height: 48px; color: var(--white); transform: rotate(-3.5deg); transform-origin: left bottom; }
  .offer { left: 34px; font-family: "Roboto Condensed", "Arial Narrow", sans-serif; font-weight: 800; font-size: 48px; line-height: 58px; color: var(--white); text-shadow: 2px 2px 0 #222; }
  .offer--free { top: 231px; color: var(--yellow); }
  .offer--session { top: 290px; }
  .offer--call { top: 365px; font-size: 46px; line-height: 56px; }
  .valid-box { position: absolute; left: 27px; top: 438px; width: 354px; height: 78px; background: var(--white); border: 2px solid var(--black); box-shadow: 4px 4px 0 #222; font-size: 30px; line-height: 1; color: var(--black); padding: 22px 16px; word-spacing: 30px; }
  .benefits { left: 682px; top: 225px; font-family: "Roboto Condensed", "Arial Narrow", sans-serif; font-weight: 700; text-shadow: 2px 2px 0 #222; }
  .benefits h2 { font: inherit; font-size: 34px; line-height: 40px; color: var(--white); }
  .benefits ul { list-style: none; font-size: 37px; color: var(--yellow); line-height: 71px; margin-top: 17px; }
</style>
</head>
<body>

<section class="card card--contact" aria-label="Trainer business card">
  <svg class="card__art" viewBox="0 0 1075 539" preserveAspectRatio="none" aria-hidden="true">
    <polygon points="0,0 690,0 0,120" fill="var(--orange)"/>
    <polygon points="700,0 790,0 360,80 345,66" fill="var(--black)"/>
    <line x1="0" y1="34" x2="200" y2="0" stroke="var(--white)" stroke-width="3"/>
    <line x1="300" y1="40" x2="560" y2="0" stroke="var(--white)" stroke-width="2"/>
    <polygon points="590,539 1075,450 1075,539" fill="var(--black)"/>
    <polygon points="720,539 1075,480 1075,539" fill="var(--orange)"/>
    <line x1="820" y1="539" x2="1075" y2="497" stroke="var(--white)" stroke-width="3"/>
  </svg>
  <div class="ghost-art" role="img" aria-label="Faint background of leaping athlete silhouettes"></div>

  <div class="brand card__text"><span class="brand__mark"></span>Kestrel</div>

  <p class="card__text label contact-label">Contact Details:</p>
  <h1 class="card__text person-name">Marisol Quintero</h1>
  <p class="card__text person-role">Director &amp; Head Personal Trainer</p>
  <ul class="card__text contact-list">
    <li>p 1300 555 072</li>
    <li>m 0400 555 319</li>
    <li>e marisol@kestrelfitness.com.au</li>
    <li>w www.kestrelfitness.com.au</li>
  </ul>

  <div class="card__text side-col">
    <div class="side-block side-block--feature">
      <p class="label label--orange">Chatterbox Feature:</p>
      <ul><li>Join the Kestrel Online</li><li>Competitions, Special Deals,</li><li>Hints, Tips + More</li></ul>
    </div>
    <div class="side-block side-block--tag">
      <p class="label label--orange">Tagline:</p>
      <ul><li>No Judgements</li><li>No Limits</li></ul>
    </div>
    <div class="side-block side-block--services">
      <p class="label label--orange">Our Services:</p>
      <ul><li>Personal Training</li><li>Fitness Classes</li><li>Boot Camps</li><li>Events &amp; Adventures</li><li>Corporate Fitness</li></ul>
    </div>
  </div>
</section>

<section class="card card--promo" aria-label="Personal training promo card">
  <svg class="card__art" viewBox="0 0 1075 539" preserveAspectRatio="none" aria-hidden="true">
    <polygon points="0,22 480,0 520,0 0,34" fill="var(--white)"/>
    <polygon points="0,52 960,0 890,160 0,205" fill="var(--white)"/>
    <polygon points="0,137 872,74 872,165 0,205" fill="var(--black)"/>
    <line x1="895" y1="150" x2="1075" y2="108" stroke="var(--white)" stroke-width="4"/>
    <line x1="700" y1="539" x2="1075" y2="470" stroke="var(--white)" stroke-width="4"/>
    <line x1="760" y1="539" x2="1075" y2="492" stroke="var(--white)" stroke-width="3"/>
  </svg>
  <div class="ghost-art ghost-art--promo" role="img" aria-label="Faint background of leaping athlete silhouettes"></div>

  <h1 class="card__text promo-title">PERSONAL TRAINING</h1>
  <p class="card__text promo-strap">Want to Get Fit &amp; Into Shape? Let Us Show You How</p>

  <p class="card__text offer offer--free">FREE Initial Consult &amp; 30min</p>
  <p class="card__text offer offer--session">1-on-1 Session (valued $80.00)</p>
  <p class="card__text offer offer--call">Call 1300 555 072 Now To Book</p>
  <div class="valid-box">Valid: / /</div>

  <div class="card__text benefits">
    <h2>Key Benefits of Kestrel:</h2>
    <ul><li>No Boring Workouts</li><li>No Long Term Contracts</li><li>Results Guaranteed</li></ul>
  </div>
</section>

</body>
</html>
```